Music Producer Website

I need a website designed for my music production company. We specialize in finding talented musicians and matching them with music producers all over the United States. A visitor can create a profile and/or upload their music demo and we submit it to thousands of music producers and production companies for review. In many cases, our members will receive multiple signing offers from music producers allowing them to choose the contract that is best for them. "We turn aspiring musicians into SuperStars!"
Please include photos that reflect all genres of music (black artists, white artists, both male and female.) We produce all types of music including rap, R&B, rock, country, and Hip Hop.
When a user creates a profile, they become visible to thousands of record producers who are looking to sign new talent and make them stars.
Somewhere in the top half of the page, please include a small form that the visitor can fill out. The form should look as follows:
Title (large and bold): Contact Us or Submit Music Demo
Fields to include (* = required): First Name*, Last Name*, Age, Zip Code, Email Address*, Daytime Phone, Evening Phone, Comments
Then, there will be a "submit" button to proceed to next step of form. Just below the "submit" button, should be the following verbiage: "After submitting, you will have the opportunity to upload demos of your music (optional) and provide other pertinent information about yourself, band, or group."
Updates
Reason: I have not seen a design that I am 100% satisfied with yet. Ideally, rotating header images (GIF or other) with several different music producers in studio (male, female, black, white) would be perfect. Here are some examples of how the header pics could look:
http://files.pixelmarlo.com/entry_img/503912/640287/640287_7315064_503912_image.jpg
http://files.pixelmarlo.com/entry_img/503912/640287/640287_7315079_503912_image.jpg
http://files.pixelmarlo.com/entry_img/503912/640287/640287_7315055_503912_image.jpg
Also, there should be a form on the site (somewhere in upper half of the page) with the following headline:
GET FOUND AND BECOME A STAR! (super large, super-bold font)
Contact Us or Submit Your Music for Review (large font, not as bold as headline)
First Name
Last Name
Age
Zip Code
Email Address
Daytime Phone
Evening Phone
Comments
Target Market(s)
We are targeting all types of musicians including rock, rap, pop, R&B, country, gospel, etc.
Industry/Entity Type
Artists
Colors
Designer to choose colors to be used in the design.
Look and feel
Each slider illustrates characteristics of the customer's brand and the style your logo design should communicate.

```html
<!DOCTYPE html>
<html lang="en">
<head>
<meta charset="utf-8">
<title>Vantage Music Productions</title>
<link href="https://fonts.googleapis.com/css2?family=Cinzel:wght@400;700&family=Ubuntu:wght@300;400;500;700&display=swap" rel="stylesheet">
<style>
:root{
  --ink:#070707;
  --panel:#141414;
  --gold:#c9a75a;
  --gold-field:#5e4714;
  --text-soft:#b9a575;
  --text-head:#c9ad66;
}
*{margin:0;padding:0;box-sizing:border-box}
html,body{width:793px;height:1200px;overflow:hidden;background:var(--ink)}
body{position:relative;font-family:"Ubuntu",sans-serif;color:var(--text-soft)}
.abs{position:absolute}
.caps{font-family:"Cinzel",serif}

/* header */
.site-header{left:0;top:0;width:793px;height:78px;background:var(--ink)}
.brand{left:58px;top:0;width:164px;height:78px;background:var(--panel);display:flex;flex-direction:column;align-items:center;justify-content:center;gap:1px}
.brand-name{font-family:"Cinzel",serif;font-size:26px;color:var(--gold);letter-spacing:1px;line-height:1}
.brand-sub{font-family:"Cinzel",serif;font-size:7px;color:var(--gold);letter-spacing:1.6px}
.main-nav a{position:absolute;top:46px;font-family:"Cinzel",serif;font-size:10px;color:var(--gold);text-decoration:none;letter-spacing:.4px}
.auth-btn{top:14px;height:16px;font-family:"Cinzel",serif;font-size:8px;display:flex;align-items:center;justify-content:center;border:1px solid #999}
.btn-signup{left:597px;width:51px;background:linear-gradient(#f2f2f2,#b9b9b9);color:#222}
.btn-login{left:654px;width:52px;background:linear-gradient(#f0dd97,#c69f46);color:#2a1e05}

/* hero */
.hero{left:0;top:78px;width:793px;height:332px;overflow:hidden;
  background:
    radial-gradient(ellipse 120px 200px at 355px 200px,rgba(196,30,36,.95) 0%,rgba(150,20,28,.7) 45%,rgba(150,20,28,0) 100%),
    radial-gradient(ellipse 60px 50px at 395px 60px,rgba(214,160,130,.7) 0%,rgba(214,160,130,0) 100%),
    radial-gradient(ellipse 90px 60px at 360px 310px,rgba(150,160,190,.6) 0%,rgba(150,160,190,0) 100%),
    radial-gradient(circle at 260px 20px,rgba(190,200,255,.85) 0%,rgba(110,120,200,.45) 18%,rgba(60,60,140,0) 40%),
    radial-gradient(ellipse 160px 140px at 100px 180px,rgba(40,50,130,.8) 0%,rgba(40,50,130,0) 100%),
    linear-gradient(90deg,#10123a 0%,#1c1e52 35%,#120a18 62%,#060606 78%,#080808 100%)}
.hero-tagline{left:109px;top:227px;font-family:"Cinzel",serif;font-size:13px;color:#fff;letter-spacing:.3px;text-shadow:0 1px 3px rgba(0,0,0,.8)}
.demo-title{left:521px;top:104px;font-size:10.5px;color:var(--text-head);letter-spacing:.5px}
.demo-form{left:522px;top:122px;width:185px;height:256px;background:linear-gradient(#8c6f2e,#6e5622);border:1px solid #a88a45}
.field{position:absolute;background:var(--gold-field);border:1px solid #7a6026;font-size:8px;color:#d6bb74;padding:5px 6px}
.btn-submit{left:577px;top:347px;width:75px;height:20px;background:linear-gradient(#e6c160,#a57f22);border:1px solid #d5b463;border-radius:2px;color:#1e1505;font-size:8px;font-weight:700;display:flex;align-items:center;justify-content:center}
.slider-track{left:79px;top:389px;width:627px;height:10px;border-radius:5px;background:linear-gradient(#9a7d3c,#5e4a1e);border:1px solid #b2924c}
.slider-thumb{left:80px;top:390px;width:40px;height:8px;border-radius:4px;background:#3a3120}

/* partners */
.partners{left:0;top:410px;width:793px;height:58px;background:var(--gold);display:flex;align-items:center;justify-content:center;gap:24px}
.partner{font-weight:700;font-size:17px;color:#111}

/* sections */
.section-title{font-family:"Cinzel",serif;font-size:10.5px;color:var(--text-head);letter-spacing:.8px}
.pager-arrow{top:482px;width:16px;height:15px;background:var(--gold);display:flex;align-items:center;justify-content:center}
.demo-card{position:absolute;width:106px}
.thumb{position:relative;width:106px;height:82px;border:1px solid #8c7542;box-shadow:inset 0 0 18px rgba(0,0,0,.55)}
.play{position:absolute;left:50%;top:50%;transform:translate(-50%,-50%)}
.demo-meta{font-size:7.5px;line-height:14px;margin-top:5px;color:var(--text-soft);padding-left:1px}
.pagination{left:191px;top:1104px;display:flex;gap:5px}
.page{height:15px;min-width:16px;padding:0 4px;background:linear-gradient(#e4cf8c,#b8953f);color:#3a2c0c;font-size:7.5px;display:flex;align-items:center;justify-content:center}
.page.wide{width:32px}

.list-item{position:absolute;left:475px;width:232px}
.list-thumb{position:absolute;left:0;top:0;width:67px;height:59px;border:1px solid #8c7542;box-shadow:inset 0 0 14px rgba(0,0,0,.5)}
.list-title{position:absolute;left:76px;top:9px;font-size:9px;color:var(--text-head);white-space:nowrap}
.list-text{position:absolute;left:76px;top:28px;font-size:7.5px;line-height:13px;color:#d8cba6;width:150px}
.btn-more{left:649px;width:57px;height:20px;background:linear-gradient(#e8d497,#b5923f);color:#2f230a;font-family:"Cinzel",serif;font-size:7px;font-weight:700;display:flex;align-items:center;justify-content:center;border:1px solid #d9bf76}

.review{position:absolute;left:472px;width:240px}
.review-thumb{position:absolute;left:0;top:0;width:67px;height:59px;border:1px solid #8c7542;box-shadow:inset 0 0 14px rgba(0,0,0,.5)}
.review-text{position:absolute;left:88px;top:0;width:150px;font-size:7.5px;line-height:16px;color:var(--text-soft)}
.stars{position:absolute;left:88px;top:44px;display:flex;gap:4px}

/* footer */
.site-footer{left:0;top:1146px;width:793px;height:54px;background:var(--gold)}
.footer-nav{left:86px;top:12px;font-family:"Cinzel",serif;font-size:8.5px;color:#2a1f08;letter-spacing:.3px}
.footer-nav span{margin:0 8px}
.copyright{left:88px;top:33px;font-family:"Cinzel",serif;font-size:8px;color:#2a1f08}
.social{top:1164px;width:22px;height:22px;border-radius:50%;background:#1a1408}
</style>
</head>
<body>
<svg width="0" height="0" style="position:absolute">
  <defs>
    <symbol id="star" viewBox="0 0 20 20"><polygon points="10,1 12.6,7.2 19.3,7.6 14.1,11.8 15.8,18.4 10,14.8 4.2,18.4 5.9,11.8 0.7,7.6 7.4,7.2" fill="#c9a55a"/></symbol>
    <symbol id="play" viewBox="0 0 24 24"><circle cx="12" cy="12" r="11" fill="#1b1b1b" fill-opacity=".75" stroke="#fff" stroke-width="1.6"/><polygon points="9.5,7 17,12 9.5,17" fill="#fff"/></symbol>
  </defs>
</svg>

<header class="site-header abs">
  <div class="brand abs"><div class="brand-name">VANTAGE</div><div class="brand-sub">MUSIC PRODUCTIONS</div></div>
  <nav class="main-nav">
    <a style="left:316px">Home</a>
    <a style="left:368px">About Us</a>
    <a style="left:431px">Create a Profile</a>
    <a style="left:540px">Music Producers</a>
    <a style="left:651px">Contact Us</a>
  </nav>
  <div class="auth-btn btn-signup abs">SIGN UP</div>
  <div class="auth-btn btn-login abs">LOGIN</div>
</header>

<section class="hero abs" role="img" aria-label="Stage photo of a female singer in a red top performing with a microphone under blue concert lights"></section>
<div class="hero-tagline abs">We turn aspiring musicians into SuperStars!</div>

<div class="demo-title abs caps">Submit Music Demo</div>
<form class="demo-form abs"></form>
<div class="field" style="left:534px;top:132px;width:161px;height:22px">First Name</div>
<div class="field" style="left:534px;top:158px;width:161px;height:22px">Last Name</div>
<div class="field" style="left:534px;top:184px;width:161px;height:22px">E-Mail</div>
<div class="field" style="left:534px;top:210px;width:45px;height:21px">Age</div>
<div class="field" style="left:586px;top:210px;width:109px;height:21px">Zip- Code</div>
<div class="field" style="left:534px;top:236px;width:161px;height:22px">Daytime Phone</div>
<div class="field" style="left:534px;top:262px;width:161px;height:21px">Evening Phone</div>
<div class="field" style="left:534px;top:288px;width:161px;height:52px">Comments</div>
<div class="btn-submit abs">SUBMIT</div>
<div class="slider-track abs"></div>
<div class="slider-thumb abs"></div>

<div class="partners abs">
  <span class="partner">Northbeam</span>
  <span class="partner">Ironring</span>
  <span class="partner">Amplify TV</span>
  <span class="partner">Halo Box</span>
  <span class="partner">Crest</span>
  <span class="partner">Circlehouse</span>
  <span class="partner">Stonegate</span>
</div>

<div class="section-title abs" style="left:80px;top:482px">LATEST UPLOADED MUSIC DEMOS</div>
<div class="pager-arrow abs" style="left:394px"><svg width="8" height="8"><polygon points="7,0 7,8 0,4" fill="#111"/></svg></div>
<div class="pager-arrow abs" style="left:414px"><svg width="8" height="8"><polygon points="1,0 1,8 8,4" fill="#111"/></svg></div>

<div class="demo-card" style="left:86px;top:516px"><div class="thumb" role="img" aria-label="Male rock singer on a teal-lit stage" style="background:radial-gradient(circle at 75% 30%,rgba(120,220,230,.7),rgba(0,0,0,0) 45%),radial-gradient(ellipse at 40% 60%,#2a3a4a,rgba(0,0,0,0) 60%),linear-gradient(135deg,#1f5a6c,#0a1a24)"><svg class="play" width="26" height="26"><use href="#play"/></svg></div><div class="demo-meta">Name : George mark<br>Song : I will also be<br>Time : 1.45</div></div>
<div class="demo-card" style="left:205px;top:516px"><div class="thumb" role="img" aria-label="Blonde female pop singer on a purple stage" style="background:radial-gradient(ellipse at 45% 40%,rgba(230,190,120,.9),rgba(0,0,0,0) 50%),radial-gradient(circle at 70% 80%,rgba(200,140,110,.7),rgba(0,0,0,0) 50%),linear-gradient(135deg,#5a1a6a,#b33a8a)"><svg class="play" width="26" height="26"><use href="#play"/></svg></div><div class="demo-meta">Name : George mark<br>Song : I will also be<br>Time : 1.45</div></div>
<div class="demo-card" style="left:323px;top:516px"><div class="thumb" role="img" aria-label="Singer with platinum hair in black and white" style="background:radial-gradient(ellipse at 65% 30%,#f2f2f2,rgba(255,255,255,0) 45%),radial-gradient(circle at 60% 80%,#5a5a5a,rgba(0,0,0,0) 50%),linear-gradient(135deg,#1a1a1a,#3a3a3a)"><svg class="play" width="26" height="26"><use href="#play"/></svg></div><div class="demo-meta">Name : George mark<br>Song : I will also be<br>Time : 1.45</div></div>

<div class="demo-card" style="left:86px;top:664px"><div class="thumb" role="img" aria-label="Rapper in sunglasses performing under blue lights" style="background:radial-gradient(circle at 15% 25%,rgba(90,140,230,.9),rgba(0,0,0,0) 40%),radial-gradient(ellipse at 60% 55%,rgba(180,120,80,.8),rgba(0,0,0,0) 55%),linear-gradient(135deg,#1a2a55,#2a1a10)"><svg class="play" width="26" height="26"><use href="#play"/></svg></div><div class="demo-meta">Name : George mark<br>Song : I will also be<br>Time : 1.45</div></div>
<div class="demo-card" style="left:205px;top:664px"><div class="thumb" role="img" aria-label="Male rock vocalist at a microphone in monochrome" style="background:radial-gradient(ellipse at 75% 40%,#cfcfcf,rgba(0,0,0,0) 50%),radial-gradient(circle at 25% 65%,#6a6a6a,rgba(0,0,0,0) 45%),linear-gradient(135deg,#2a2a2a,#111)"><svg class="play" width="26" height="26"><use href="#play"/></svg></div><div class="demo-meta">Name : George mark<br>Song : I will also be<br>Time : 1.45</div></div>
<div class="demo-card" style="left:323px;top:664px"><div class="thumb" role="img" aria-label="Female singer in a dark dress with warm stage light" style="background:radial-gradient(circle at 80% 25%,rgba(240,220,190,.9),rgba(0,0,0,0) 40%),radial-gradient(ellipse at 45% 50%,rgba(170,110,90,.8),rgba(0,0,0,0) 50%),linear-gradient(135deg,#2a1a16,#4a3a30)"><svg class="play" width="26" height="26"><use href="#play"/></svg></div><div class="demo-meta">Name : George mark<br>Song : I will also be<br>Time : 1.45</div></div>

<div class="demo-card" style="left:86px;top:810px"><div class="thumb" role="img" aria-label="Red-haired female rock singer with a microphone" style="background:radial-gradient(ellipse at 40% 60%,rgba(240,130,40,.95),rgba(0,0,0,0) 45%),radial-gradient(circle at 45% 25%,rgba(220,70,40,.9),rgba(0,0,0,0) 30%),linear-gradient(135deg,#2a4a8a,#1a2a4a)"><svg class="play" width="26" height="26"><use href="#play"/></svg></div><div class="demo-meta">Name : George mark<br>Song : I will also be<br>Time : 1.45</div></div>
<div class="demo-card" style="left:205px;top:810px"><div class="thumb" role="img" aria-label="Blonde female singer on a blue-lit stage" style="background:radial-gradient(ellipse at 65% 30%,rgba(240,220,170,.9),rgba(0,0,0,0) 40%),radial-gradient(circle at 45% 75%,rgba(80,180,160,.7),rgba(0,0,0,0) 45%),linear-gradient(135deg,#1a2a5a,#4a6aa4)"><svg class="play" width="26" height="26"><use href="#play"/></svg></div><div class="demo-meta">Name : George mark<br>Song : I will also be<br>Time : 1.45</div></div>
<div class="demo-card" style="left:323px;top:810px"><div class="thumb" role="img" aria-label="Masked metal vocalist under orange light" style="background:radial-gradient(circle at 10% 15%,rgba(250,190,90,.95),rgba(0,0,0,0) 45%),radial-gradient(ellipse at 75% 55%,rgba(30,30,30,.9),rgba(0,0,0,0) 55%),linear-gradient(135deg,#b0601a,#140c06)"><svg class="play" width="26" height="26"><use href="#play"/></svg></div><div class="demo-meta">Name : George mark<br>Song : I will also be<br>Time : 1.45</div></div>

<div class="demo-card" style="left:86px;top:964px"><div class="thumb" role="img" aria-label="Young male country singer in a studio" style="background:radial-gradient(ellipse at 50% 40%,rgba(200,170,140,.8),rgba(0,0,0,0) 40%),radial-gradient(circle at 15% 20%,rgba(150,160,180,.7),rgba(0,0,0,0) 35%),linear-gradient(135deg,#3a3028,#1a1612)"><svg class="play" width="26" height="26"><use href="#play"/></svg></div><div class="demo-meta">Name : George mark<br>Song : I will also be<br>Time : 1.45</div></div>
<div class="demo-card" style="left:205px;top:964px"><div class="thumb" role="img" aria-label="Performer under bright pink and violet stage lights" style="background:radial-gradient(ellipse at 70% 40%,rgba(255,190,240,.9),rgba(0,0,0,0) 40%),radial-gradient(circle at 20% 80%,rgba(255,60,180,.9),rgba(0,0,0,0) 50%),linear-gradient(135deg,#2a10a0,#8a2ad0)"><svg class="play" width="26" height="26"><use href="#play"/></svg></div><div class="demo-meta">Name : George mark<br>Song : I will also be<br>Time : 1.45</div></div>
<div class="demo-card" style="left:323px;top:964px"><div class="thumb" role="img" aria-label="Female soul singer in black and white" style="background:radial-gradient(ellipse at 70% 35%,#bdbdbd,rgba(0,0,0,0) 40%),radial-gradient(circle at 80% 80%,#555,rgba(0,0,0,0) 40%),linear-gradient(135deg,#050505,#1e1e1e)"><svg class="play" width="26" height="26"><use href="#play"/></svg></div><div class="demo-meta">Name : George mark<br>Song : I will also be<br>Time : 1.45</div></div>

<div class="pagination abs">
  <span class="page wide">Prev</span><span class="page">1</span><span class="page">2</span><span class="page">3</span><span class="page">4</span><span class="page">5</span><span class="page">6</span><span class="page">…</span><span class="page">22</span><span class="page wide">Next</span>
</div>

<div class="section-title abs" style="left:472px;top:482px">LIST OF SELECTED MUSICS</div>
<div class="list-item" style="top:518px"><div class="list-thumb" role="img" aria-label="Male rocker with guitar on a red stage" style="background:radial-gradient(circle at 30% 30%,rgba(240,120,60,.9),rgba(0,0,0,0) 45%),radial-gradient(ellipse at 60% 70%,#2a1a18,rgba(0,0,0,0) 60%),linear-gradient(135deg,#c0401a,#3a0a08)"><svg class="play" width="26" height="26"><use href="#play"/></svg></div><div class="list-title">Neque porro quisquam est qui</div><div class="list-text">Lorem Ipsum is simply dummy text of the printing and typesetting industry.</div></div>
<div class="list-item" style="top:603px"><div class="list-thumb" role="img" aria-label="Female singer under yellow and red lights" style="background:radial-gradient(circle at 30% 25%,rgba(240,110,60,.9),rgba(0,0,0,0) 40%),radial-gradient(ellipse at 70% 70%,rgba(230,200,80,.9),rgba(0,0,0,0) 55%),linear-gradient(135deg,#b08a2a,#8a3a1a)"><svg class="play" width="26" height="26"><use href="#play"/></svg></div><div class="list-title">Neque porro quisquam est qui</div><div class="list-text">Lorem Ipsum is simply dummy text of the printing and typesetting industry.</div></div>
<div class="list-item" style="top:688px"><div class="list-thumb" role="img" aria-label="Dark-haired female singer against a red backdrop" style="background:radial-gradient(ellipse at 45% 40%,rgba(200,150,130,.75),rgba(0,0,0,0) 40%),radial-gradient(circle at 80% 20%,rgba(200,30,40,.9),rgba(0,0,0,0) 50%),linear-gradient(135deg,#6a1018,#1a1010)"><svg class="play" width="26" height="26"><use href="#play"/></svg></div><div class="list-title">Neque porro quisquam est qui</div><div class="list-text">Lorem Ipsum is simply dummy text of the printing and typesetting industry.</div></div>
<div class="btn-more abs" style="top:769px">READ MORE</div>

<div class="section-title abs" style="left:473px;top:822px">LATEST &nbsp;REVIEWS</div>
<div class="review" style="top:856px"><div class="review-thumb" role="img" aria-label="Blonde pop singer in a striped top" style="background:radial-gradient(ellipse at 60% 40%,rgba(240,220,180,.9),rgba(0,0,0,0) 45%),radial-gradient(circle at 20% 20%,rgba(200,200,210,.6),rgba(0,0,0,0) 35%),linear-gradient(135deg,#2a2a2e,#4a4a50)"></div><div class="review-text">Sed ut perspiciatis unde omnis iste natus error sit voluptatem accusantium</div><div class="stars"><svg width="15" height="15"><use href="#star"/></svg><svg width="15" height="15"><use href="#star"/></svg><svg width="15" height="15"><use href="#star"/></svg><svg width="15" height="15"><use href="#star"/></svg><svg width="15" height="15"><use href="#star"/></svg></div></div>
<div class="review" style="top:945px"><div class="review-thumb" role="img" aria-label="Blonde female singer under warm red light" style="background:radial-gradient(ellipse at 55% 45%,rgba(250,210,150,.95),rgba(0,0,0,0) 50%),linear-gradient(135deg,#a01a14,#5a0a08)"></div><div class="review-text">Sed ut perspiciatis unde omnis iste natus error sit voluptatem accusantium</div><div class="stars"><svg width="15" height="15"><use href="#star"/></svg><svg width="15" height="15"><use href="#star"/></svg><svg width="15" height="15"><use href="#star"/></svg><svg width="15" height="15"><use href="#star"/></svg><svg width="15" height="15"><use href="#star"/></svg></div></div>
<div class="review" style="top:1025px"><div class="review-thumb" role="img" aria-label="Dark-haired female singer performing under red light" style="background:radial-gradient(ellipse at 50% 45%,rgba(210,150,130,.7),rgba(0,0,0,0) 40%),radial-gradient(circle at 20% 80%,rgba(230,40,40,.9),rgba(0,0,0,0) 50%),linear-gradient(135deg,#b82020,#3a0a0a)"></div><div class="review-text">Sed ut perspiciatis unde omnis iste natus error sit voluptatem accusantium</div><div class="stars"><svg width="15" height="15"><use href="#star"/></svg><svg width="15" height="15"><use href="#star"/></svg><svg width="15" height="15"><use href="#star"/></svg><svg width="15" height="15"><use href="#star"/></svg><svg width="15" height="15"><use href="#star"/></svg></div></div>
<div class="btn-more abs" style="top:1102px">READ MORE</div>

<footer class="site-footer abs">
  <div class="footer-nav abs">Home<span>|</span>About Us<span>|</span>Create a Profile<span>|</span>Music Producers<span>|</span>Contact Us</div>
  <div class="copyright abs">Copyright ©2013 &nbsp;Company Name &nbsp;&nbsp;- All Rights Reserved</div>
</footer>
<div class="social abs" style="left:634px"></div>
<div class="social abs" style="left:660px"></div>
<div class="social abs" style="left:686px"></div>
</body>
</html>
```